General Contractor Website Design

We are working with a General Contractor in California that specializes in building custom kitchens, baths, and homes for high-end clients.

Here are some websites for inspiration:
https://morvelstudio.example/
https://ridgelanebuildworks.example
https://www.framequill.example
https://www.nestiva.example
https://www.tzdwell.example
https://rplresidences.example

Thank you for taking the time to consider designing a website for us. We are web developers based in Stockton, CA, USA. Most of our projects go through the same process. Understanding this process may help you win a project with us. We custom-code all of our websites in-house. We don’t have any requirements as to what tools you use for your design, but we ask that you follow these guidelines.

IMAGES:
If you use any images or icons in the design, we ask that you have a link to the asset so we can purchase the image/icon. Most of the designs we submit do not have the customer’s images on them unless they have some great images. Be creative; show us the feeling you are trying to portray with your image choices. Use any royalty-free site you choose. We subscribe to Velqor and mainly use their images, but we can purchase images outside of Velqor. PLEASE NOTE: we will not submit designs to clients with watermarks on the images.

FONTS:
We ask that you identify the fonts you’re using in the design. This can be done in a message if you want. We typically use Google Fonts and Velqor Fonts.

CONTENT:
We're always open to different content and ideas. We often submit designs with stock images so the client can see our vision. We typically take pictures after the website launch to use their images with our vision. Lorem Ipsum is fine for paragraphs, but we ask that you make the Headers with correct English. We want to be able to show the vision and identify the sections of the website.

INSPIRATION:
We typically add a couple of links in the brief of websites we like to help you get started in your design.

REVISIONS:
We do not often ask for revisions of the designs unless we see something in the design that may not appeal to the client. If there are slight changes that we want to make, we do that in the development process.

FEEDBACK:
We rarely give feedback on designs during the design process. We are working on many website projects and do not have the time to provide feedback. We usually respond if your request is well thought out and asks specific questions, but a note asking “feedback, please” usually goes unanswered.

```html
<!DOCTYPE html>
<html lang="en">
<head>
<meta charset="utf-8">
<title>Ashford Structures — Custom Homes, Kitchens &amp; Baths</title>
<link rel="stylesheet" href="https://fonts.googleapis.com/css2?family=Red+Hat+Display:wght@400;500;600;700&family=Crimson+Text:wght@400;600&display=swap">
<style>
:root{
  --red:#e3202c;
  --ink:#1d1d1d;
  --text:#333;
  --muted:#666;
  --paper:#ffffff;
  --soft:#f5f4f4;
  --charcoal:#2d2d2d;
  --slate:#3a3d3e;
  --line:#d6d6d6;
  --head:"Red Hat Display", sans-serif;
  --body:"Crimson Text", serif;
}
*{box-sizing:border-box;margin:0;padding:0}
html,body{width:1200px;height:4082px;overflow:hidden}
body{position:relative;background:var(--paper);font-family:var(--body);color:var(--text)}
.abs{position:absolute}
.brand{font-family:var(--head);font-weight:700;color:var(--red);font-size:12px;letter-spacing:1px;display:flex;align-items:center;gap:7px;text-transform:uppercase;white-space:nowrap}
.brand-mark{width:12px;height:12px;background:var(--red)}

/* nav */
.site-nav{left:0;top:0;width:1200px;height:81px;background:var(--paper)}
.nav-links a{position:absolute;top:32px;font-family:var(--head);font-weight:600;font-size:12px;color:var(--ink);text-decoration:none}
.nav-links a.active{color:var(--red)}
.btn{display:flex;align-items:center;justify-content:center;background:var(--red);color:#fff;font-family:var(--head);font-weight:600;font-size:12px;border-radius:2px;text-decoration:none}

/* hero */
.hero{left:0;top:81px;width:1200px;height:515px;background:linear-gradient(90deg,#4a4c4d 0%,#3a3d3e 45%,#2f3233 100%)}
.hero-photo{position:absolute;left:0;top:0;width:620px;height:515px;background:radial-gradient(ellipse at 45% 70%,#7b7670 0%,#5a5855 35%,rgba(58,61,62,0) 70%)}
.hero h1{position:absolute;left:683px;top:117px;width:285px;font-family:var(--head);font-weight:700;font-size:27px;line-height:34px;color:#fff}
.hero .lede{position:absolute;left:683px;top:234px;font-size:14px;line-height:19px;color:#e8e8e8}
.hero .btn{position:absolute;left:683px;top:287px;width:135px;height:33px;font-size:11px}
.social{position:absolute;left:683px;top:342px;display:flex;align-items:center;gap:8px;font-size:11px;color:#bbb}
.social i{width:16px;height:16px;border-radius:50%;border:1.5px solid #ddd;display:inline-block}

/* about */
.about{left:0;top:596px;width:1200px;height:273px;background:var(--soft);text-align:center}
.sec-title{font-family:var(--head);font-weight:700;color:var(--ink)}
.underline{display:block;height:3px;background:var(--red)}
.about h2{position:absolute;left:0;width:1200px;top:62px;font-size:27px}
.about .underline{position:absolute;left:546px;top:100px;width:60px}
.about p{position:absolute;left:288px;top:117px;width:625px;font-size:13.5px;line-height:19px;color:var(--ink)}

/* services */
.crafted h2{left:225px;top:930px;font-size:26px}
.crafted .underline{left:225px;top:966px;width:75px}
.crafted .sub{left:225px;top:983px;font-size:13px;color:var(--ink)}
.feature-img{position:absolute}
.counter{position:absolute;font-size:11px;color:#777}
.feature h3{position:absolute;font-family:var(--head);font-weight:700;font-size:16px;line-height:21px;color:var(--ink)}
.feature .bar{position:absolute;width:75px;height:3px;background:var(--red)}
.feature h4{position:absolute;font-size:13px;font-weight:400;color:var(--ink)}
.feature p{position:absolute;width:325px;font-size:12px;line-height:16.5px;color:#444}

/* stats */
.stats{left:0;top:1813px;width:1200px;height:376px;background:var(--charcoal)}
.stat{position:absolute;top:140px;color:#fff}
.stat b{display:block;font-family:var(--head);font-weight:500;font-size:46px;line-height:50px}
.stat span{font-size:12px;color:#ddd}
.worker{position:absolute;left:740px;top:26px;width:238px;height:350px;background:linear-gradient(180deg,#c9362c 0%,#b98a6b 35%,#8c8c8c 65%,#6e6558 100%);border-radius:110px 110px 0 0}

/* gallery */
.gallery-head h2{left:0;width:1200px;text-align:center;top:2250px;font-size:17px}
.gallery-head .underline{left:518px;top:2273px;width:75px;height:2px}
.gallery-head p{left:0;width:1200px;text-align:center;top:2284px;font-size:12px;color:var(--ink)}
.grid{left:0;top:2343px;width:1200px;height:482px;display:grid;grid-template-columns:repeat(3,1fr);grid-template-rows:repeat(3,1fr);gap:1px;background:#fff}
.grid div{position:relative}
.zoom{position:absolute;left:50%;top:50%;transform:translate(-50%,-50%);text-align:center;color:#fff;font-family:var(--head);font-size:9px}

/* testimonials */
.testimonials{left:0;top:2825px;width:1200px;height:443px;background:radial-gradient(ellipse at 50% 40%,#3b3b3b 0%,#272727 80%)}
.testimonials h2{position:absolute;left:0;width:1200px;text-align:center;top:60px;font-size:17px;color:#fff}
.testimonials .underline{position:absolute;left:548px;top:83px;width:104px;height:2px}
.card{position:absolute;top:118px;width:178px;height:195px;border:1.5px solid #cfcfcf;color:#eee;padding:12px 16px}
.avatar{width:32px;height:32px;border-radius:50%;display:inline-block;vertical-align:middle}
.stars{display:inline-block;vertical-align:middle;margin-left:8px;line-height:11px}
.stars b{color:#f6b800;font-size:14px;letter-spacing:-1px}
.stars small{display:block;font-family:var(--head);font-size:6.5px;color:#ddd}
.card h5{font-family:var(--head);font-weight:500;font-size:8.5px;margin:10px 0 12px}
.card p{font-size:10px;line-height:14.5px}
.pager{position:absolute;left:535px;top:346px;display:flex;align-items:center;gap:10px}
.dot{width:7px;height:7px;border-radius:50%;background:#ccc}
.dot.on{background:var(--red)}

/* contact */
.form-card{left:531px;top:3332px;width:415px;height:386px;background:var(--charcoal);color:#fff;text-align:center}
.form-card h2{font-family:var(--head);font-weight:500;font-size:20px;margin-top:30px}
.form-card p{font-size:12px;line-height:19px;margin:10px auto 0;width:270px;color:#ddd}
.field{position:absolute;left:104px;width:241px;height:22px;background:#fff;border-radius:2px;font-size:9px;color:#888;text-align:left;padding:5px 12px}
.form-card .btn{position:absolute;left:104px;top:324px;width:93px;height:33px;font-size:11px}
.info-card{left:254px;top:3379px;width:317px;height:292px;background:var(--soft);box-shadow:0 4px 14px rgba(0,0,0,.18);text-align:center}
.info-card h2{font-family:var(--head);font-weight:500;font-size:20px;color:var(--ink);margin-top:34px}
.info-card .intro{font-size:12px;line-height:17px;color:#444;margin:8px auto 0;width:190px}
.info-row{position:absolute;left:50px;display:flex;gap:14px;font-size:9.5px;line-height:15px;color:#333;text-align:left;width:200px}

/* footer */
.footer-rule{left:0;top:3783px;width:1200px;height:1px;background:var(--line)}
.f-head{position:absolute;top:3838px;font-family:var(--head);font-weight:600;font-size:11px;color:var(--red)}
.f-links a{position:absolute;font-size:10.5px;color:var(--ink);text-decoration:none}
.f-social{left:268px;top:3866px;display:flex;gap:9px}
.f-social i{width:14px;height:14px;border-radius:50%;background:var(--ink);display:block}
.newsletter-input{left:799px;top:3882px;width:179px;height:34px;background:#d9d9d9;font-size:9px;color:#888;padding:11px 13px}
.newsletter-btn{left:799px;top:3932px;width:179px;height:32px}
.legal-rule{left:225px;top:4048px;width:753px;height:1px;background:var(--line)}
.legal{position:absolute;top:4061px;font-family:var(--head);font-size:7.5px;color:#333}
</style>
</head>
<body>

<header class="site-nav abs">
  <div class="brand abs" style="left:225px;top:34px"><span class="brand-mark"></span>Ashford Structures</div>
  <nav class="nav-links">
    <a class="active" href="#" style="left:554px">Home</a>
    <a href="#" style="left:613px">About Us</a>
    <a href="#" style="left:690px">Services</a>
    <a href="#" style="left:765px">Portfolio</a>
  </nav>
  <a class="btn abs" href="#" style="left:858px;top:24px;width:118px;height:33px">Contact Us</a>
</header>

<section class="hero abs">
  <div class="hero-photo" role="img" aria-label="Dark panelled living room with a grey boucle armchair, potted plant and brass floor lamp"></div>
  <h1>Crafting Homes with Unmatched Attention to Detail</h1>
  <p class="lede">Transforming Houses into Homes:<br>Where Memories Flourish</p>
  <a class="btn" href="#">View Our Work</a>
  <div class="social">Social Links&nbsp; <i></i><i></i><i></i></div>
</section>

<section class="about abs">
  <h2 class="sec-title">About Us</h2>
  <span class="underline"></span>
  <p>At Ashford Structures, we are passionate about transforming houses into homes, creating extraordinary living spaces that reflect your unique personality and style. As a leading general contractor specializing in custom kitchens, baths, and homes, we bring together a perfect blend of innovative design, superior craftsmanship, and unparalleled attention to detail.</p>
</section>

<section class="crafted">
  <h2 class="sec-title abs">Crafted with Care, Designed for Life</h2>
  <span class="underline abs"></span>
  <p class="sub abs">Building Dream Homes and Dream Kitchens</p>

  <div class="feature">
    <div class="feature-img" role="img" aria-label="Modern white villa with a swimming pool" style="left:225px;top:1057px;width:371px;height:187px;background:linear-gradient(180deg,#9fc3e0 0%,#e8ecee 40%,#7a8b6f 70%,#2f7fa6 100%)"></div>
    <span class="counter" style="left:576px;top:1248px">1/3</span>
    <h3 style="left:634px;top:1086px">Custom Homes that Exceed Expectations</h3>
    <span class="bar" style="left:634px;top:1110px"></span>
    <h4 style="left:634px;top:1125px">Turning Your Vision into an Architectural Reality</h4>
    <p style="left:634px;top:1148px">Trust us to build your dream home. We transform your vision into meticulously designed and expertly constructed residences. Experience the joy of living in a home tailored to your style, where every detail is perfected.</p>
  </div>

  <div class="feature">
    <h3 style="left:225px;top:1321px">Custom Kitchens for Inspired Chefs</h3>
    <span class="bar" style="left:225px;top:1345px"></span>
    <h4 style="left:225px;top:1360px">Unleash the Full Potential of Your Kitchen Space</h4>
    <p style="left:225px;top:1383px;width:335px">Elevate your cooking experience with our custom kitchen designs. Our expert team combines functionality and beauty, paying meticulous attention to every detail. From tailored cabinetry to innovative storage solutions, we create kitchens that inspire creativity and reflect your unique style.</p>
    <div class="feature-img" role="img" aria-label="Bright kitchen with walnut cabinetry, island and pendant lights" style="left:609px;top:1301px;width:369px;height:189px;background:linear-gradient(90deg,#8a5a36 0%,#e9e6e1 35%,#f2f0ec 65%,#8a5a36 100%)"></div>
    <span class="counter" style="left:609px;top:1493px">2/3</span>
  </div>

  <div class="feature">
    <div class="feature-img" role="img" aria-label="Marble bathroom with vanity and glass shower" style="left:225px;top:1547px;width:371px;height:187px;background:linear-gradient(90deg,#6f5c45 0%,#a18a6c 40%,#4b3f33 75%,#2c2823 100%)"></div>
    <span class="counter" style="left:576px;top:1738px">3/3</span>
    <h3 style="left:624px;top:1565px;width:350px">Transforming Bathrooms into Personal Sanctuaries</h3>
    <span class="bar" style="left:624px;top:1610px"></span>
    <h4 style="left:624px;top:1625px">Designing Your Private Oasis for Relaxation and Renewal</h4>
    <p style="left:624px;top:1648px">Create your own sanctuary with our luxurious bathroom designs. We blend style and functionality, incorporating elegant fixtures and spa-like features. Immerse yourself in a space designed for relaxation and renewal.</p>
  </div>
</section>

<section class="stats abs">
  <div class="stat" style="left:224px"><b>127+</b><span>Successful Projects</span></div>
  <div class="stat" style="left:427px"><b>81</b><span>Satisfied Clients</span></div>
  <div class="stat" style="left:601px"><b>5+</b><span>Years of Experience</span></div>
  <div class="worker" role="img" aria-label="Smiling builder in a red hard hat with arms crossed"></div>
</section>

<section class="gallery-head">
  <h2 class="sec-title abs">Our Project Gallery</h2>
  <span class="underline abs"></span>
  <p class="abs">View our project gallery for you home inspiration</p>
</section>

<div class="grid abs">
  <div role="img" aria-label="Kitchen with island" style="background:linear-gradient(135deg,#8a6b52,#c9c4bd,#5b4d42)">
    <div class="zoom"><svg width="30" height="30" viewBox="0 0 30 30" fill="none" stroke="#fff" stroke-width="2.5"><circle cx="12" cy="12" r="9"/><path d="M19 19l8 8M12 8v8M8 12h8"/></svg><br>Zoom In</div>
  </div>
  <div role="img" aria-label="Marble bathroom" style="background:linear-gradient(135deg,#7a6550,#b09a7e,#3b342d)"></div>
  <div role="img" aria-label="White villa by a pool" style="background:linear-gradient(180deg,#a6c9e2,#eef0f0,#6f8b63,#3a8bb3)"></div>
  <div role="img" aria-label="White living room with fireplace" style="background:linear-gradient(135deg,#f2f2f0,#dadad6,#b8b6b0)"></div>
  <div role="img" aria-label="Green wall with console and plants" style="background:linear-gradient(135deg,#2f4a3d,#3f5e4e,#23372d)"></div>
  <div role="img" aria-label="Dining room with staircase" style="background:linear-gradient(135deg,#e7e9eb,#b9c1c7,#3c4a5a)"></div>
  <div role="img" aria-label="Modern house with pool" style="background:linear-gradient(180deg,#eceae6,#a07c5a,#4f8fa8)"></div>
  <div role="img" aria-label="Modern house with palm trees" style="background:linear-gradient(135deg,#9cc4de,#f0f0ee,#4f7a3a)"></div>
  <div role="img" aria-label="White kitchen with range hood" style="background:linear-gradient(135deg,#f4f3f1,#d8d4ce,#8d8379)"></div>
</div>

<section class="testimonials abs">
  <h2 class="sec-title">Testimonials</h2>
  <span class="underline"></span>

  <article class="card" style="left:225px">
    <span class="avatar" role="img" aria-label="Customer portrait" style="background:#a88b72"></span><span class="stars"><b>★★★★★</b><small>4.5 Star Rating</small></span>
    <h5>Nora P.</h5>
    <p>I hired Willowbend Constructions to remodel my kitchen and they did an excellent job. Their pricing was fair and their work was outstanding</p>
  </article>
  <article class="card" style="left:416px">
    <span class="avatar" role="img" aria-label="Customer portrait" style="background:#5a6170"></span><span class="stars"><b>★★★★★</b><small>4.0 Star Rating</small></span>
    <h5>Marcus T.</h5>
    <p>Willowbend Constructions did an amazing job on my home renovation. They were fast, efficient, and professional from start to finish. Highly recommended!</p>
  </article>
  <article class="card" style="left:607px">
    <span class="avatar" role="img" aria-label="Customer portrait" style="background:#8c8c8c"></span><span class="stars"><b>★★★★★</b><small>4.5 Star Rating</small></span>
    <h5>Lena V.</h5>
    <p>Willowbend Constructions exceeded my expectations on every level. I would definitely work with them again in the future.</p>
  </article>
  <article class="card" style="left:797px">
    <span class="avatar" role="img" aria-label="Customer portrait" style="background:#7a3b34"></span><span class="stars"><b>★★★★★</b><small>4.5 Star Rating</small></span>
    <h5>Owen K.</h5>
    <p>Willowbend Constructions is a company that truly takes pride in their work. They are passionate about what they do and it shows in the quality of their work</p>
  </article>

  <div class="pager">
    <svg width="30" height="30" viewBox="0 0 30 30" fill="none" stroke="#fff" stroke-width="2"><circle cx="15" cy="15" r="13"/><path d="M21 15H9M14 10l-5 5 5 5"/></svg>
    <span class="dot"></span><span class="dot on"></span><span class="dot"></span>
    <svg width="30" height="30" viewBox="0 0 30 30" fill="none" stroke="#fff" stroke-width="2"><circle cx="15" cy="15" r="13"/><path d="M9 15h12M16 10l5 5-5 5"/></svg>
  </div>
</section>

<section class="form-card abs">
  <h2>Get In Touch</h2>
  <p>Please fill out the form below and we'll get back to you as soon as possible.</p>
  <div class="field" style="top:134px">Name</div>
  <div class="field" style="top:178px">Email Address</div>
  <div class="field" style="top:222px;height:87px">Message</div>
  <a class="btn" href="#">Submit</a>
</section>

<section class="info-card abs">
  <h2>Contact Us</h2>
  <p class="intro">We'd love to hear from you! Here's how to get in touch</p>
  <div class="info-row" style="top:114px">
    <svg width="12" height="14" viewBox="0 0 12 14" fill="none" stroke="#333" stroke-width="1.4"><path d="M6 13s5-4.5 5-8A5 5 0 0 0 1 5c0 3.5 5 8 5 8z"/><circle cx="6" cy="5" r="1.7"/></svg>
    <span>Willowbend Construction 88 Harbor Lane Suite 210 Lodi, CA 95240</span>
  </div>
  <div class="info-row" style="top:176px">
    <svg width="12" height="12" viewBox="0 0 12 12" fill="none" stroke="#333" stroke-width="1.4"><circle cx="6" cy="6" r="2"/><path d="M8 6v1a2 2 0 0 0 3 0V6a5 5 0 1 0-2 4"/></svg>
    <span>hello@ashfordstructures.example</span>
  </div>
  <div class="info-row" style="top:222px">
    <svg width="12" height="12" viewBox="0 0 12 12" fill="none" stroke="#333" stroke-width="1.4"><path d="M2 1h2.5l1 3-1.5 1a7 7 0 0 0 3 3l1-1.5 3 1V10a1 1 0 0 1-1 1A10 10 0 0 1 1 2a1 1 0 0 1 1-1z"/></svg>
    <span>(555) 014-2290</span>
  </div>
</section>

<footer>
  <div class="footer-rule abs"></div>
  <div class="brand abs" style="left:225px;top:3840px"><span class="brand-mark"></span>Ashford Structures</div>
  <div class="f-social abs"><i></i><i></i><i></i></div>

  <span class="f-head" style="left:431px">Navigations</span>
  <nav class="f-links">
    <a href="#" style="left:431px;top:3878px">Home</a>
    <a href="#" style="left:431px;top:3909px">FAQ</a>
    <a href="#" style="left:431px;top:3941px">Blog</a>
    <a href="#" style="left:431px;top:3973px">Portfolio</a>
    <a href="#" style="left:431px;top:4004px">Contact Us</a>
  </nav>

  <span class="f-head" style="left:601px">Our Services</span>
  <nav class="f-links">
    <a href="#" style="left:601px;top:3878px">Remodeling Kitchen</a>
    <a href="#" style="left:601px;top:3909px">New Home Construction</a>
    <a href="#" style="left:601px;top:3941px">Interior &amp; Exterior Painting</a>
    <a href="#" style="left:601px;top:3973px">Fire and Water Damage</a>
    <a href="#" style="left:601px;top:4004px">Custom built-ins and trim</a>
  </nav>

  <span class="f-head" style="left:799px">NEWSLETTER</span>
  <div class="newsletter-input abs">Enter Your Email...</div>
  <a class="btn newsletter-btn abs" href="#">Submit</a>

  <div class="legal-rule abs"></div>
  <span class="legal" style="left:225px">All Rights Reserved</span>
  <span class="legal" style="left:547px">© 2023, Ashford Structures</span>
  <span class="legal" style="left:860px">Terms Conditions | Privacy &amp; Policy</span>
</footer>

</body>
</html>
```